KTV Lanternfall

I need a graphic package design for our new bodybuilding sports supplement. The artwork should be clean and useable for many formats. examples or great usage are www.ferrovigorlab.example, www.quartzpulse.example and http://www.belwinnutrition.example/ as examples. I am adding our logo for your reference. The name Lanternfall is because it will help make "Big Guns" as a catch phrase, the product line will have other supplements such as creatine and protein powders and the artwork should be useable on all products. You can see our website for ideas at www.kestovalife.example
Updates

Hi everyone, There are some nice entries coming in. I do wonder if some of you are reading the brief as a few labels don't even highlight the product, KTV is the company, Lanternfall is the Product. Thanks Tam

Industry/Entity Type

Supplement

```html
<!DOCTYPE html>
<html lang="en">
<head>
<meta charset="utf-8">
<title>KTV Lanternfall – Label</title>
<link rel="stylesheet" href="https://fonts.googleapis.com/css2?family=Audiowide&family=Exo+2:wght@700&display=swap">
<style>
  :root {
    --page: #ffffff;
    --label-black: #0b0c0c;
    --label-charcoal: #2a2b2b;
    --lime: #8fe21f;
    --lime-bright: #b8ff3a;
    --lime-deep: #4aa50e;
    --white: #ffffff;
    --grey-text: #9a9a9a;
  }
  html, body {
    margin: 0;
    padding: 0;
    width: 909px;
    height: 1200px;
    overflow: hidden;
    background: var(--page);
  }
  .canvas {
    position: relative;
    width: 909px;
    height: 1200px;
  }
  .label {
    position: absolute;
    left: 120px;
    top: 360px;
    width: 670px;
    height: 570px;
    background: radial-gradient(ellipse at 50% 40%, var(--label-charcoal) 0%, var(--label-black) 70%);
    border-top: 8px solid var(--lime);
    border-bottom: 8px solid var(--lime);
    box-sizing: border-box;
    overflow: hidden;
  }
  .label-floor {
    position: absolute;
    left: 0;
    right: 0;
    bottom: 0;
    height: 150px;
    background: linear-gradient(180deg, rgba(40,40,40,0) 0%, #1c1d1d 60%, #151616 100%);
  }
  .brand {
    position: absolute;
    top: 40px;
    left: 0;
    right: 0;
    text-align: center;
    font-family: "Exo 2", sans-serif;
    font-weight: 700;
    color: var(--white);
  }
  .brand-mark {
    font-size: 62px;
    line-height: 1;
    letter-spacing: 2px;
  }
  .brand-company {
    margin-top: 6px;
    font-size: 15px;
    letter-spacing: 3px;
  }
  .light-streaks {
    position: absolute;
    left: 0;
    top: 150px;
    width: 670px;
    height: 230px;
  }
  .product-name {
    position: absolute;
    top: 225px;
    left: 0;
    right: 0;
    text-align: center;
    font-family: "Audiowide", sans-serif;
    font-size: 76px;
    line-height: 1;
    color: var(--lime);
    background: linear-gradient(180deg, var(--lime-bright) 0%, var(--lime) 55%, var(--lime-deep) 100%);
    -webkit-background-clip: text;
    background-clip: text;
    -webkit-text-fill-color: transparent;
  }
</style>
</head>
<body>
<main class="canvas">
  <section class="label">
    <div class="label-floor"></div>

    <div class="brand">
      <div class="brand-mark">KTV</div>
      <div class="brand-company">KESTOVA LIFE</div>
    </div>

    <svg class="light-streaks" viewBox="0 0 670 230" aria-hidden="true">
      <defs>
        <linearGradient id="streak" x1="0" x2="1">
          <stop offset="0" stop-color="#8fe21f" stop-opacity="0"/>
          <stop offset="0.5" stop-color="#8fe21f" stop-opacity="0.9"/>
          <stop offset="1" stop-color="#8fe21f" stop-opacity="0"/>
        </linearGradient>
      </defs>
      <rect x="210" y="24" width="250" height="2" fill="url(#streak)"/>
      <rect x="150" y="44" width="370" height="3" fill="url(#streak)"/>
      <rect x="110" y="62" width="450" height="2" fill="url(#streak)"/>
      <rect x="140" y="168" width="390" height="2" fill="url(#streak)"/>
      <rect x="190" y="186" width="290" height="3" fill="url(#streak)"/>
      <rect x="250" y="204" width="170" height="2" fill="url(#streak)"/>
    </svg>

    <h1 class="product-name">Lanternfall</h1>
  </section>
</main>
</body>
</html>
```